Banners for a bowtie/tie Fashion shop

I need banners (770x100) for a necktie and bowtie shop (http://www.kelorin.dk)

5 BOWTIE BANNERS:

I need the 3 text versions for eatch bowtie banner:

Danmarks største udvalg af butterfly
Køb butterfly. FRI fragt og FRI retur
Butterfly fra 199,- inkl. FRI fragt

5 NECKTIE BANNERS:

I need the 3 text versions for eatch necktie banner:

Danmarks største udvalg af slips
Køb slips. FRI fragt og FRI retur
Slips fra 199,- inkl. FRI fragt

All banners should contain the logo. All in JPG format and Photoshop/Inddesign/illustrator format

Target Market(s)

Guys and Gays

Industry/Entity Type

Shop

Requirements
Must have
• Logo
Nice to have
• Nice new pictures

```html
<!DOCTYPE html>
<html lang="da">
<head>
<meta charset="utf-8">
<title>Kelorin – banners</title>
<link rel="stylesheet" href="https://fonts.googleapis.com/css2?family=Source+Sans+3:wght@400;600;700&display=swap">
<style>
  :root {
    --stage: #2a2a2a;
    --wood-dark: #5a3e28;
    --wood-mid: #8a6646;
    --wood-light: #a7845f;
    --text-light: #ffffff;
    --text-dark: #2e2e2e;
    --text-mid: #444444;
    --caption-bg: rgba(40, 28, 20, 0.72);
    --button-dark: #2f2a26;
    --button-grey: #555555;
    --paper: #f3f3f3;
    --divider: #c9c9c9;
  }
  * { box-sizing: border-box; margin: 0; padding: 0; }
  html, body { width: 1200px; height: 778px; overflow: hidden; }
  body {
    background: var(--stage);
    font-family: "Source Sans 3", sans-serif;
    position: relative;
  }
  .banner {
    position: absolute;
    left: 132px;
    width: 947px;
    overflow: hidden;
    box-shadow: 0 3px 8px rgba(0,0,0,0.55);
  }
  .banner--bowtie {
    top: 245px;
    height: 123px;
    background: linear-gradient(90deg, var(--wood-dark), var(--wood-mid) 35%, var(--wood-light) 60%, var(--wood-mid) 85%, var(--wood-dark));
  }
  .banner--necktie {
    top: 400px;
    height: 135px;
    background: var(--paper);
  }
  .photo { position: absolute; top: 0; height: 100%; }
  .banner--bowtie .photo {
    left: 0; width: 268px;
    background: linear-gradient(180deg, #9c7a58 0%, #b58a6a 45%, #3a2a22 100%);
  }
  .banner--necktie .photo {
    left: 0; width: 717px;
    background: linear-gradient(90deg, #e2e2e2 0%, #bcbcbc 12%, #e9e9e9 26%, #f1f1f1 60%, #dcdcdc 100%);
  }
  .copy { position: absolute; text-align: right; }
  .banner--bowtie .copy { right: 212px; top: 12px; color: var(--text-light); }
  .banner--bowtie .line {
    display: inline-block;
    background: var(--caption-bg);
    font-size: 20px;
    line-height: 26px;
    padding: 0 6px;
    margin-bottom: 4px;
  }
  .banner--bowtie .price {
    font-size: 20px;
    font-weight: 600;
    margin-top: 2px;
    text-shadow: 0 1px 3px rgba(0,0,0,0.6);
  }
  .price strong { font-weight: 700; font-size: 34px; letter-spacing: 0.5px; }
  .banner--necktie .copy { right: 273px; top: 20px; color: var(--text-dark); }
  .heading { font-size: 19px; font-weight: 700; letter-spacing: 0.6px; line-height: 24px; }
  .sub { font-size: 20px; color: var(--text-mid); line-height: 24px; }
  .banner--necktie .price {
    display: inline-block;
    margin-top: 10px;
    padding: 0 4px 0 8px;
    background: rgba(255,255,255,0.75);
    font-size: 21px;
    color: var(--text-mid);
  }
  .banner--necktie .price strong { font-size: 29px; color: var(--text-dark); }
  .divider {
    position: absolute; left: 717px; top: 25px;
    width: 1px; height: 92px; background: var(--divider);
  }
  .brand {
    position: absolute;
    font-size: 40px;
    font-weight: 600;
    letter-spacing: -0.5px;
    line-height: 44px;
  }
  .banner--bowtie .brand { left: 772px; top: 10px; color: var(--text-light); }
  .banner--necktie .brand { left: 757px; top: 22px; color: var(--text-mid); }
  .cta {
    position: absolute;
    width: 155px; height: 37px;
    display: flex; align-items: center; justify-content: center;
    color: var(--text-light);
    font-size: 16px; font-weight: 600; letter-spacing: 0.4px;
    text-decoration: none;
  }
  .banner--bowtie .cta { left: 770px; top: 71px; background: var(--button-dark); }
  .banner--necktie .cta { left: 752px; top: 80px; background: var(--button-grey); }
</style>
</head>
<body>

<section class="banner banner--bowtie">
  <div class="photo" role="img" aria-label="Photo of a bearded man adjusting his bowtie in front of a wooden wall"></div>
  <div class="copy">
    <span class="line">Danmarks største udvalg af butterfly</span><br>
    <span class="line">Køb butterfly. FRI fragt og FRI retur</span>
    <p class="price">Butterfly fra <strong>199,- inkl. FRI fragt</strong></p>
  </div>
  <span class="brand">kelorin</span>
  <a class="cta" href="http://www.kelorin.dk">LÆS MERE &gt;&gt;</a>
</section>

<section class="banner banner--necktie">
  <div class="photo" role="img" aria-label="Photo of a man in a grey suit and black tie before a faded city skyline"></div>
  <div class="copy">
    <p class="heading">DANMARKS STØRSTE UDVALG AF SLIPS</p>
    <p class="sub">Køb slips. FRI fragt og FRI retur</p>
    <p class="price">Slips fra <strong>199,- inkl. FRI fragt</strong></p>
  </div>
  <span class="divider"></span>
  <span class="brand">kelorin</span>
  <a class="cta" href="http://www.kelorin.dk">LÆS MERE &gt;&gt;</a>
</section>

</body>
</html>
```